Plumbing and heating business card design

i need a new business card for the company i work for called Dr. Brightpipe. It is a plumbing and heating company that has been operating for over 30 years. We are not like these big plumbing companies that have ways to charge the customer as much as possible. Our company does only what is necessary and what is needed to do the job right the first time without the high cost. we are a neighborhood business which kind of explains why we don't charge customers through the roof. I would like to see a design with a nice background anything but just plain white. maybe like a light blue at the top of the design. on the back of the card i would like it to say " T. Vandermeer's Dr. Brightpipe". maybe add some color to the lettering on the front of the card for example blue font for plumbing and red font for heating. raised print. im sure Cardolux designers will make it look good. The final design should help spread a good word about our company and help grow business.

Industry/Entity Type

Business

Contact Information for Business Card

Dr. Brightpipe, Plumbing & heating, Gordon Tasker, Northeast District Operations manager, 4827 Birchwell st., Office:(555)-284-1937, doctorbrightpipe@mailverra.net

Requirements
Must have
• raised print finish and a nice sturdy feel.

```html
<!DOCTYPE html>
<html lang="en">
<head>
<meta charset="utf-8">
<title>Dr. Brightpipe – Business Card</title>
<link href="https://fonts.googleapis.com/css2?family=Open+Sans:wght@400;700;800&display=swap" rel="stylesheet">
<style>
  :root {
    --backdrop: #e9ebee;
    --card: #ffffff;
    --sky: #00b4ec;
    --sky-mid: #3fa9e0;
    --sky-light: #a9dcf5;
    --ink: #3c3c3c;
    --ink-soft: #555a60;
    --plumbing-blue: #1e88d8;
    --mark-grey: #4a4a4a;
    --rule: #dcdfe3;
  }
  * { box-sizing: border-box; margin: 0; padding: 0; }
  html, body {
    width: 1200px; height: 900px; overflow: hidden;
    background: var(--backdrop);
    font-family: "Open Sans", Arial, sans-serif;
  }
  .canvas { position: relative; width: 1200px; height: 900px; }

  .card {
    position: absolute;
    width: 560px; height: 320px;
    background: var(--card);
    box-shadow: 0 6px 18px rgba(0,0,0,.12);
    overflow: hidden;
  }
  .card--front { left: 320px; top: 100px; }
  .card--back  { left: 320px; top: 480px; }

  .swoosh { position: absolute; inset: 0; width: 100%; height: 100%; }

  .brand {
    position: absolute;
    display: flex; flex-direction: column; align-items: center;
  }
  .brand__name {
    font-weight: 800; color: var(--mark-grey);
    line-height: 1.05; text-align: center;
  }
  .brand__tagline {
    font-weight: 700; color: var(--plumbing-blue);
    letter-spacing: .5px; margin-top: 4px;
  }
  .brand__dot {
    border-radius: 50%; background: var(--mark-grey);
    margin-top: 10px;
  }

  .card--front .brand { left: 170px; top: 150px; width: 310px; }
  .card--front .brand__name { font-size: 34px; }
  .card--front .brand__tagline { font-size: 19px; }
  .card--front .brand__dot { width: 46px; height: 46px; }

  .card--back .brand { left: 28px; top: 118px; width: 260px; }
  .card--back .brand__name { font-size: 24px; }
  .card--back .brand__tagline { font-size: 13px; }
  .card--back .brand__dot { width: 30px; height: 30px; }

  .divider { position: absolute; inset: 0; width: 100%; height: 100%; }

  .contact { position: absolute; left: 318px; top: 46px; width: 232px; }
  .contact__name { font-size: 17px; font-weight: 700; color: var(--plumbing-blue); }
  .contact__role { font-size: 11.5px; color: var(--ink-soft); margin-bottom: 18px; }
  .contact__list { list-style: none; }
  .contact__item {
    display: flex; align-items: flex-start; gap: 8px;
    font-size: 11px; color: var(--ink-soft); line-height: 1.35;
    margin-bottom: 6px;
  }
  .contact__icon {
    flex: none; width: 14px; height: 14px; border-radius: 2px;
    background: var(--sky-mid);
    display: flex; align-items: center; justify-content: center;
    margin-top: 1px;
  }
</style>
</head>
<body>
<main class="canvas">

  <section class="card card--front" aria-label="Card front">
    <svg class="swoosh" viewBox="0 0 560 320" preserveAspectRatio="none" aria-hidden="true">
      <path d="M0 0 H560 V58 C420 60 220 110 0 225 Z" fill="var(--sky)"/>
      <path d="M0 200 C200 100 380 66 560 58 V72 C380 82 200 120 0 236 Z" fill="var(--sky-mid)"/>
      <path d="M0 222 C200 120 380 84 560 72 V84 C380 96 200 136 0 250 Z" fill="var(--sky-light)"/>
    </svg>
    <div class="brand">
      <p class="brand__name">T. Vandermeer's<br>Dr. Brightpipe</p>
      <p class="brand__tagline">PLUMBING &amp; HEATING</p>
      <span class="brand__dot" aria-hidden="true"></span>
    </div>
  </section>

  <section class="card card--back" aria-label="Card back">
    <svg class="divider" viewBox="0 0 560 320" aria-hidden="true">
      <line x1="300" y1="0" x2="395" y2="320" stroke="var(--rule)" stroke-width="1.5"/>
    </svg>
    <div class="brand">
      <p class="brand__name">T. Vandermeer's<br>Dr. Brightpipe</p>
      <p class="brand__tagline">PLUMBING &amp; HEATING</p>
      <span class="brand__dot" aria-hidden="true"></span>
    </div>
    <div class="contact">
      <p class="contact__name">Gordon Tasker</p>
      <p class="contact__role">Operations manager</p>
      <ul class="contact__list">
        <li class="contact__item">
          <span class="contact__icon"><svg width="9" height="10" viewBox="0 0 9 10"><path d="M4.5 0.5a3.2 3.2 0 0 1 3.2 3.2c0 2.3-3.2 5.8-3.2 5.8S1.3 6 1.3 3.7A3.2 3.2 0 0 1 4.5 0.5z" fill="#fff"/><circle cx="4.5" cy="3.7" r="1.2" fill="var(--sky-mid)"/></svg></span>
          <span>Northeast District ,<br>4827 Birchwell st.</span>
        </li>
        <li class="contact__item">
          <span class="contact__icon"><svg width="9" height="9" viewBox="0 0 9 9"><path d="M1.5 0.8l1.6 0 .7 2-1 .8a5 5 0 0 0 2.6 2.6l.8-1 2 .7v1.6c0 .5-.4.8-.9.8A7.6 7.6 0 0 1 .7 1.7c0-.5.3-.9.8-.9z" fill="#fff"/></svg></span>
          <span>(555)-284-1937</span>
        </li>
        <li class="contact__item">
          <span class="contact__icon"><svg width="10" height="8" viewBox="0 0 10 8"><rect x="0.5" y="0.5" width="9" height="7" rx="1" fill="#fff"/><path d="M0.8 1l4.2 3.3L9.2 1" stroke="var(--sky-mid)" fill="none" stroke-width="1"/></svg></span>
          <span>doctorbrightpipe@mailverra.net</span>
        </li>
      </ul>
    </div>
  </section>

</main>
</body>
</html>
```